IT Tradingsystem for car dealers needs Business Card Design

We need a fresh and modern design for our new business cards.

We develop a it-business system for car dealers in Sweden, Norway and on our way down to further countries in Europe, hence the namechange to BrolaTek Europe AB. The site can be found at www.brolatek-example.com. The startpage is also in for an update/modernization soon so don't take to much from here.

We are looking to print double sided, 4-colour cards.

We want to look professional, modern and serious. Open to cooler suggestions, but not too crazy. We need to make a good and serious impression on our potential customers. It needs to reflect our scandinavian design values and layout.

Preferably with the full BrolaTek logo in good size on the back, so the small print on the logo can be read easily.

Text that needs to go on the cards:
-------

Per Oskar Fjellström
Founder

Direct +46 70-512 96 47
Support 08-612 57 394
po.fjellstrom@brolatek-example.com

BrolaTek Europe AB
Box 8617
104 29 Stockholm

Brolatek-example.com
Saljportalen-example.se

--------
Good luck and thanks!

PS. If you need more input or see what our previous cards looked like, don't hesitate to contact me!

Target Market(s)

Decision makers / executives at brand cardealers

Industry/Entity Type

Automotive

Contact Information for Business Card

Normal size

Requirements
Must have
• Full logo
Nice to have
• Base on our orange colors
Should not have
• No fonts with serif, and not too much graphics

```html
<!DOCTYPE html>
<html lang="sv">
<head>
<meta charset="utf-8">
<title>BrolaTek Europe AB – Business Card</title>
<link rel="stylesheet" href="https://fonts.googleapis.com/css2?family=Montserrat:wght@400;500;600;700&display=swap">
<style>
  :root {
    --bg: #2b2b2d;
    --card: #0b0b0b;
    --orange: #f47b20;
    --white: #ffffff;
    --grey: #e6e6e6;
  }
  * { margin: 0; padding: 0; box-sizing: border-box; }
  html, body { width: 1200px; height: 900px; overflow: hidden; }
  body {
    background: var(--bg);
    font-family: "Montserrat", Arial, sans-serif;
    position: relative;
  }
  .card {
    position: absolute;
    width: 640px;
    height: 366px;
    background: var(--card);
    border-radius: 18px;
    overflow: hidden;
  }
  .card-back { left: 60px; top: 70px; }
  .card-front { left: 500px; top: 464px; }
  .card-bands { position: absolute; inset: 0; width: 100%; height: 100%; }

  /* Back */
  .back-brand {
    position: absolute;
    left: 0; right: 0; top: 118px;
    display: flex; align-items: center; justify-content: center; gap: 16px;
  }
  .brand-square { display: block; background: var(--orange); }
  .back-brand .brand-square { width: 50px; height: 50px; }
  .back-brand .brand-name {
    color: var(--orange); font-weight: 700; font-size: 54px; letter-spacing: -1px;
  }

  /* Front */
  .front-brand {
    position: absolute; left: 40px; top: 108px;
    display: flex; align-items: center; gap: 14px;
  }
  .front-brand .brand-square { width: 44px; height: 44px; }
  .front-brand .brand-name {
    color: var(--white); font-weight: 700; font-size: 50px; line-height: 1; letter-spacing: -1px;
  }
  .brand-tagline {
    color: var(--white); font-size: 13px; font-weight: 500; margin-top: 4px; letter-spacing: 0.2px;
  }
  .person {
    position: absolute; right: 40px; top: 68px; width: 240px; text-align: right;
  }
  .person-name { color: var(--orange); font-weight: 700; font-size: 21px; }
  .person-role { color: var(--white); font-size: 14px; margin-top: 2px; }
  .person-rule { height: 1.5px; background: var(--orange); margin: 8px 0 10px; }
  .company-name { color: var(--orange); font-weight: 600; font-size: 15px; }
  .company-line { color: var(--white); font-size: 15px; line-height: 1.3; }

  .contact {
    position: absolute; left: 40px; top: 236px; width: 320px;
  }
  .contact-rule { height: 1.5px; background: var(--orange); margin-bottom: 8px; }
  .contact-list { list-style: none; }
  .contact-item {
    display: flex; align-items: center; gap: 12px;
    color: var(--white); font-size: 14.5px; line-height: 18px;
  }
  .contact-item svg { width: 11px; height: 11px; fill: var(--orange); flex: none; }
  .contact-item strong { font-weight: 700; }
</style>
</head>
<body>

  <section class="card card-back" aria-label="Card back">
    <svg class="card-bands" viewBox="0 0 640 366" aria-hidden="true">
      <polygon points="0,322 292,322 274,366 0,366" fill="var(--orange)"/>
      <polygon points="282,350 640,350 640,366 276,366" fill="var(--white)"/>
    </svg>
    <div class="back-brand">
      <span class="brand-square"></span>
      <span class="brand-name">BrolaTek</span>
    </div>
  </section>

  <section class="card card-front" aria-label="Card front">
    <svg class="card-bands" viewBox="0 0 640 366" aria-hidden="true">
      <polygon points="426,316 640,316 640,366 406,366" fill="var(--orange)"/>
      <polygon points="0,350 414,350 408,366 0,366" fill="var(--white)"/>
    </svg>

    <div class="front-brand">
      <span class="brand-square"></span>
      <div>
        <div class="brand-name">BrolaTek</div>
        <div class="brand-tagline">KollTest | Remarketing | saljportalen-example.se</div>
      </div>
    </div>

    <div class="person">
      <div class="person-name">Per Oskar Fjellström</div>
      <div class="person-role">Founder</div>
      <div class="person-rule"></div>
      <div class="company-name">BrolaTek Europe AB</div>
      <div class="company-line">Box 8617</div>
      <div class="company-line">104 29 Stockholm</div>
    </div>

    <div class="contact">
      <div class="contact-rule"></div>
      <ul class="contact-list">
        <li class="contact-item">
          <svg viewBox="0 0 12 12"><path d="M2.5 0.5 L4.5 0.5 L5.2 3 L3.8 4.2 Q5 7 7.8 8.2 L9 6.8 L11.5 7.5 L11.5 9.5 Q11.5 11.5 9.5 11.5 Q0.5 11 0.5 2.5 Q0.5 0.5 2.5 0.5 Z"/></svg>
          +46 70-512 96 47
        </li>
        <li class="contact-item">
          <svg viewBox="0 0 12 12"><rect x="0.5" y="2" width="11" height="3" rx="1.5"/><rect x="2" y="5.5" width="8" height="5.5" rx="1"/></svg>
          08-612 57 394
        </li>
        <li class="contact-item">
          <svg viewBox="0 0 12 12"><path d="M0.5 2 H11.5 V10 H0.5 Z M1.5 3 L6 6.5 L10.5 3 Z" fill-rule="evenodd"/></svg>
          po.fjellstrom@brolatek-example.com
        </li>
        <li class="contact-item">
          <svg viewBox="0 0 12 12"><circle cx="6" cy="6" r="5.5"/></svg>
          <span>www.<strong>brolatek-example</strong>.com</span>
        </li>
      </ul>
    </div>
  </section>

</body>
</html>
```